Modern Small Law Firm Website To Look Cutting Edge

I need a website design for a new, single-attorney law firm. The firm will be called "The Thornwell Law Group." Our goal is to handle car accident and general personal injury lawsuits for individuals.

Our selling points are: (1) We charge less so you keep more; (2) We have experience and success trying and settling multi-million dollar cases; (3) We use modern technology to make the whole process simple, easy and hassle-free for clients.

Also because we are a one-man law firm, the clients will personally know the lawyer and have access to them. For that reason, I thought a good big tagline for the website would be "KNOW YOUR LAWYER"

I like the idea of splitting the website vertically down the middle, with the left side having a blue background, a picture of me, and big white lettering for the tagline, and the right side having a white background with blue lettering and headlines. I don't want navy blue or royal blue, but a more bright and eye-catching blue color. We can experiment with different shades.

I would be curious about how it could look with some minor orange accent coloring somewhere.

I need to feature prominently, probably in the top left corner, this phone number: 504-917-2083.

This will be used as much by mobile users as it would be by desktop/computer users.

The final design should communicate trust, convenience and cutting edge technology that leads to success.

Finally, I would be curious how we can have a sleek looking info submission box somewhere on the right side nearer the bottom that features different combinations of presenting these phrases: "QUICK QUESTION? QUICK ANSWER" The info submission button could say "Ask"

I am uploading two different pictures of me that can be used. The gray backgrounds are not necessary or good, if there is a way to cut them out that would be great. I can try and get that if needed.

Target Market(s)

Individuals who have been hurt by others, mostly in car accidents. They will be frustrated, inconvenienced and need to be soothed.

Industry/Entity Type

Legal

Number of Pages Required

1 page

Font styles to use
Sans Serif

Colors
0692cd
33a6d7
85cae6
faa54b
f78f20
3276b5

Requirements
Must have
• If you have started designing already, please note that the project description information is more important than the image that I uploaded originally. It has since been deleted.
• Also please now use the color photo that has been uploaded.
Nice to have
• I really want a clean and simple website design with not a lot of clutter. I'd like to avoid the typical law firm websites that you see that have tool bars across the top and basic borders/columns everywhere. It needs to grab your attention and look a little more cutting edge and different.
• Let's experiment with different eye-catching ways to present the three value propositions I noted.
• Also if the screen is split vertically with the left and right side being blue and white, maybe we can experiment with different ways that the two colors could fade into each other as opposed to just a line where one color starts and the other ends.
• And maybe the blue/white backgrounds could be textured somehow so that they don't appear flat. Perhaps we could try using differing shades of blue to give the appearance of pattern or 3D texture.
Should not have
• The basic picture/design I uploaded is just a suggestion, but there isn't really anything there.

```html
<!DOCTYPE html>
<html lang="en">
<head>
<meta charset="utf-8">
<title>The Thornwell Law Group</title>
<link href="https://fonts.googleapis.com/css2?family=Roboto:wght@300;400;500&family=Open+Sans:wght@400&display=swap" rel="stylesheet">
<style>
:root{
  --blue:#0b8fd0;
  --blue-light:#3aa4d9;
  --blue-deep:#0e6ea5;
  --orange:#e8913a;
  --orange-light:#f5a955;
  --ink:#1f1f1f;
  --muted:#777;
  --panel:#f3f3f3;
  --footer:#3a3a3a;
  --footer-base:#2f2f2f;
  --white:#fff;
}
*{margin:0;padding:0;box-sizing:border-box}
html,body{width:755px;height:1200px;overflow:hidden}
body{position:relative;font-family:'Roboto',sans-serif;background:var(--white);color:var(--ink)}
.abs{position:absolute}

/* hero */
.hero{left:0;top:0;width:755px;height:382px;background:linear-gradient(160deg,#2f3a2c 0%,#3b4636 35%,#6c706d 65%,#8b8e90 100%)}
.hero-shade{left:0;top:0;width:755px;height:382px;background:rgba(0,0,0,.25)}
.topbar{left:54px;top:0;width:646px;height:59px;border-bottom:1px solid rgba(255,255,255,.7)}
.phone{left:0;top:27px;color:var(--white);font-size:12px;display:flex;align-items:center;gap:6px}
.brand{left:0;width:646px;top:22px;text-align:center;color:var(--orange);font-size:20px;font-weight:500;letter-spacing:.2px}
.tools{right:0;top:28px;display:flex;gap:6px;align-items:center}
.tools .sq{width:11px;height:11px;background:var(--white);border-radius:2px}
.tagline{left:0;width:755px;top:160px;text-align:center;color:var(--white);font-weight:300;line-height:1}
.tagline .small{font-size:43px;display:block;letter-spacing:1px}
.tagline .big{font-size:62px;display:block;margin-top:6px;font-weight:400}
.arrow{width:24px;height:24px;border-radius:50%;background:rgba(0,0,0,.45);top:199px;display:flex;align-items:center;justify-content:center}

/* intro split */
.help{left:54px;top:401px;width:323px;height:85px;background:var(--blue);color:var(--white);text-align:center;font-size:21px;line-height:30px;padding-top:15px}
.portrait{left:54px;top:486px;width:323px;height:328px;background:radial-gradient(ellipse at 60% 40%,#9a9a9a 0%,#6f6f6f 60%,#555 100%)}
.card{left:400px;width:298px;height:61px;border:1px solid #e0e0e0;box-shadow:0 1px 2px rgba(0,0,0,.12);background:var(--white)}
.card .ring{position:absolute;left:19px;top:8px;width:43px;height:43px;border:1.5px solid var(--blue);border-radius:50%;display:flex;align-items:center;justify-content:center}
.card h3{position:absolute;left:74px;top:16px;font-size:14px;font-weight:400}
.card p{position:absolute;left:75px;top:36px;font-size:7.5px;color:var(--muted)}
.ask-box{left:402px;top:623px;width:296px;height:191px;background:linear-gradient(180deg,var(--blue-light),var(--blue-deep))}
.ask-box h4{position:absolute;left:0;width:100%;top:15px;text-align:center;color:var(--white);font-weight:400;font-size:13px}
.field{position:absolute;width:130px;height:34px;background:var(--white);font-size:8px;color:#555;padding:13px 0 0 12px}
.ask-btn{position:absolute;left:16px;top:121px;width:265px;height:33px;border-radius:3px;background:linear-gradient(180deg,var(--orange-light),var(--orange));color:var(--white);font-size:15px;text-align:center;line-height:33px;font-weight:500}
.ask-note{position:absolute;left:0;width:100%;top:165px;text-align:center;color:var(--white);font-size:9px}

/* values */
.values{left:0;top:833px;width:755px;height:196px;background:var(--panel)}
.divider{top:10px;width:1px;height:176px;background:#dedede}
.value{top:0;text-align:center}
.value .badge{width:66px;height:66px;border-radius:50%;background:var(--orange);border:2px solid #f2b173;margin:33px auto 0;display:flex;align-items:center;justify-content:center}
.value p{font-size:10.5px;color:var(--muted);line-height:17px;font-weight:300}

/* footer */
.footer{left:0;top:1029px;width:755px;height:133px;background:var(--footer);color:var(--white);font-family:'Open Sans',sans-serif}
.footer h5{position:absolute;font-family:'Roboto',sans-serif;font-weight:400;font-size:10px;top:25px}
.footer .txt{position:absolute;font-size:7.5px;line-height:13px}
.subscribe{position:absolute;left:427px;top:80px;display:flex}
.subscribe .input{width:107px;height:25px;background:var(--white);color:#999;font-size:7px;padding:9px 0 0 8px}
.subscribe .btn{width:51px;height:25px;background:var(--orange);font-size:10px;text-align:center;line-height:25px}
.social{position:absolute;left:619px;top:48px;display:flex;gap:11px}
.social span{width:21px;height:21px;background:#f1efe9;border-radius:2px}
.base{left:0;top:1162px;width:755px;height:38px;background:var(--footer-base);border-top:1px solid #8a6a44;color:var(--white);font-family:'Open Sans',sans-serif;font-size:8.5px;text-align:center;line-height:36px}
</style>
</head>
<body>

<header class="hero abs" role="img" aria-label="Photo of a wrecked silver car by a forest roadside"></header>
<div class="hero-shade abs"></div>

<div class="topbar abs">
  <div class="phone abs">
    <svg width="10" height="10" viewBox="0 0 10 10"><rect width="10" height="10" rx="2" fill="#fff"/><path d="M3 2.3l1 1.2-.6.8c.4.9 1 1.5 1.9 1.9l.8-.6 1.2 1-.5 1c-2.6-.2-4.4-2-4.6-4.6z" fill="#333"/></svg>
    504-917-2083
  </div>
  <div class="brand abs">THE THORNWELL LAW GROUP</div>
  <div class="tools abs">
    <svg width="11" height="10" viewBox="0 0 11 10"><rect y="1" width="11" height="1.6" fill="#fff"/><rect y="4.3" width="11" height="1.6" fill="#fff"/><rect y="7.6" width="11" height="1.6" fill="#fff"/></svg>
    <span style="width:8px"></span>
    <span class="sq"></span><span class="sq"></span><span class="sq"></span>
  </div>
</div>

<h1 class="tagline abs"><span class="small">KNOW YOUR</span><span class="big">LAWYER</span></h1>
<div class="arrow abs" style="left:29px"><svg width="8" height="10" viewBox="0 0 8 10"><path d="M6 1L2 5l4 4" stroke="#fff" stroke-width="1.4" fill="none"/></svg></div>
<div class="arrow abs" style="left:697px"><svg width="8" height="10" viewBox="0 0 8 10"><path d="M2 1l4 4-4 4" stroke="#fff" stroke-width="1.4" fill="none"/></svg></div>

<section>
  <h2 class="help abs" style="font-weight:400">CAR WRECK?<br>WE CAN HELP</h2>
  <div class="portrait abs" role="img" aria-label="Portrait photo of the attorney in a dark suit and striped tie"></div>

  <div class="card abs" style="top:405px">
    <div class="ring"><svg width="16" height="16" viewBox="0 0 16 16"><circle cx="4" cy="4" r="2.2" stroke="#0b8fd0" stroke-width="1.6" fill="none"/><circle cx="12" cy="12" r="2.2" stroke="#0b8fd0" stroke-width="1.6" fill="none"/><path d="M13 2L3 14" stroke="#0b8fd0" stroke-width="1.8"/></svg></div>
    <h3>Never more than 24%</h3>
    <p>Our lawyers will never overchargeyou like others will</p>
  </div>
  <div class="card abs" style="top:478px">
    <div class="ring"><svg width="18" height="16" viewBox="0 0 18 16"><path d="M9 1L1 5h16z" fill="#0b8fd0"/><rect x="2" y="6" width="14" height="1.4" fill="#0b8fd0"/><rect x="3" y="8" width="2" height="5" fill="#0b8fd0"/><rect x="6.3" y="8" width="2" height="5" fill="#0b8fd0"/><rect x="9.7" y="8" width="2" height="5" fill="#0b8fd0"/><rect x="13" y="8" width="2" height="5" fill="#0b8fd0"/><rect x="1" y="13.5" width="16" height="1.6" fill="#0b8fd0"/></svg></div>
    <h3>We make it easy</h3>
    <p>These new brake pads are really cool, you won't believe it.</p>
  </div>
  <div class="card abs" style="top:552px">
    <div class="ring" style="left:17px"><svg width="20" height="16" viewBox="0 0 20 16"><circle cx="10" cy="4" r="3" fill="#0b8fd0"/><circle cx="4" cy="6" r="2.3" fill="#0b8fd0"/><circle cx="16" cy="6" r="2.3" fill="#0b8fd0"/><path d="M5 15c0-4 2-6 5-6s5 2 5 6z" fill="#0b8fd0"/><path d="M0 14c0-3 1.5-5 4-5 1 0 1.6.3 2 .8-1 1-1.6 2.5-1.7 4.2z" fill="#0b8fd0"/><path d="M20 14c0-3-1.5-5-4-5-1 0-1.6.3-2 .8 1 1 1.6 2.5 1.7 4.2z" fill="#0b8fd0"/></svg></div>
    <h3 style="left:72px">Big Firm lawyering</h3>
    <p style="left:73px">With experience in multi-milliondollar litigation, we're the best.</p>
  </div>

  <form class="ask-box abs">
    <h4>QUICK QUESTION?</h4>
    <div class="field" style="left:16px;top:40px">Name</div>
    <div class="field" style="left:151px;top:40px">Email id</div>
    <div class="field" style="left:16px;top:80px">Phone</div>
    <div class="field" style="left:151px;top:80px">Message</div>
    <div class="ask-btn">ASK</div>
    <div class="ask-note">QUICK ANSWER</div>
  </form>
</section>

<section class="values abs">
  <div class="divider abs" style="left:245px"></div>
  <div class="divider abs" style="left:493px"></div>
  <div class="value abs" style="left:40px;width:186px">
    <div class="badge"><svg width="28" height="26" viewBox="0 0 28 26"><path d="M27 1L1 12l8 3 2 9 4-6 7 5z" fill="#fff"/><path d="M27 1L9 15l2 9" stroke="#e8913a" stroke-width="1.2" fill="none"/></svg></div>
    <p style="margin-top:22px">We charge less so you keep more</p>
  </div>
  <div class="value abs" style="left:270px;width:200px">
    <div class="badge"><svg width="30" height="24" viewBox="0 0 30 24"><g fill="none" stroke="#fff" stroke-width="2"><rect x="10" y="2" width="9" height="8"/><rect x="4" y="12" width="9" height="8"/><rect x="16" y="12" width="9" height="8"/></g></svg></div>
    <p style="margin-top:23px">We have experience and success trying<br>and settling multi-million dollar cases</p>
  </div>
  <div class="value abs" style="left:510px;width:198px">
    <div class="badge"><svg width="24" height="26" viewBox="0 0 24 26"><path d="M3 2h10l4 4v14H3z" fill="#fff"/><path d="M9 8h9l4 4v12H9z" fill="#fff" stroke="#e8913a" stroke-width="1.4"/></svg></div>
    <p style="margin-top:19px">We use modern technology to make the<br>whole process simple, easy and hassle-<br>free for clients</p>
  </div>
</section>

<footer class="footer abs">
  <h5 style="left:60px">CONTACT US</h5>
  <div class="txt" style="left:61px;top:48px">214 Marlow Avenue 3rd Floor<br>Brookfield, NY &nbsp;10552, &nbsp;USA</div>
  <div class="txt" style="left:62px;top:82px;font-size:10px;display:flex;gap:10px;align-items:center">
    <svg width="11" height="11" viewBox="0 0 11 11"><path d="M2 1l2 2.3-1 1.2c.7 1.5 1.8 2.6 3.3 3.3l1.2-1L10 9l-1 1.5C4.5 10.2.8 6.5.5 2z" fill="none" stroke="#fff" stroke-width=".9"/></svg>(+901) 555-0148</div>
  <div class="txt" style="left:62px;top:100px;display:flex;gap:10px;align-items:center">
    <svg width="11" height="9" viewBox="0 0 11 9"><rect x=".5" y=".5" width="10" height="8" fill="none" stroke="#fff" stroke-width=".9"/><path d="M.5.5l5 4 5-4" fill="none" stroke="#fff" stroke-width=".9"/></svg>hello@thornwellgroup.example</div>

  <h5 style="left:232px">LATEST TWEET'S</h5>
  <span class="abs" style="left:234px;top:48px;width:11px;height:11px;background:#fff;border-radius:2px"></span>
  <div class="txt" style="left:256px;top:45px;font-size:7px">Phasellus porta. Fusce susct varius<br>mi. Cum sociis natoque penabus et<br>magnis dis parturient montes, nas-<br>cetur ridiculus mus. See more here<br>http://tw.example/k4Rb2</div>

  <h5 style="left:426px">NEWSLETTER</h5>
  <div class="txt" style="left:426px;top:45px;font-size:7px">Excepteur sint occaecat cupidatat non proident,<br>sunt in culpa qui officia deserunt mollit anim</div>
  <div class="subscribe"><div class="input">Enter your email address</div><div class="btn">Sign Up</div></div>

  <h5 style="left:618px">SOCIAL MEDIA</h5>
  <div class="social"><span></span><span></span><span></span></div>
</footer>
<div class="base abs">2016 &nbsp;All Rights Reserved.</div>

</body>
</html>
```